Flyer für Online-Shop mit modernen Gartenprodukten - puristisch und hochwertig
Zielgruppe
Wir verkaufen Produkte rund um den modernen, puristischen Garten (Bauhaus-Stil), die es im Baumarkt oder Gartencenter nicht gibt. Die Produkte entstehen oft in kleinen Manufakturen, sind von hochwertiger Qualität und bewegen sich im mittleren bis höheren Preissegment.
Zielgruppe sind Leute zwischen ca. 30 und 65 Jahren, die ihren Garten oder Balkon gern modern gestalten, also eher puristisch und 'aufgeräumt' statt verspielt oder im Landhaus-Stil.
www.kiesel-und-form.de
Aufgabenstellung
Es soll ein vierseitiger Flyer im Format 21 x 21 cm erstellt werden, der als Werbemittel verteilt, an entsprechenden Orten ausgelegt, an Interessenten versendet und Zeitungen beigelegt werden soll.
Der Flyer soll hochwertig und modern aussehen - klar im Design, aber trotzdem ansprechend-inspirierend. Von der Grundtendenz eher "unbunt" - gerne in den Farben grün, grau (wie im Logo) und weiß. Dazwischen als elegante Eyecatcher aber immer wieder farbige Bilder der Produkte.
Keinesfalls aber überfrachtet und marktschreierisch, sondern zurückhaltend-dezent, das höhere Preisniveau widerspiegelnd.
Ein Briefing mit näheren Angaben zu Texten und Bildern lade ich separat hoch. Ebenso einige Fotos, die verwendet werden können. Ansonsten können Sie gerne Fotos von meiner Website für den Entwurf verwenden.

```html
<!DOCTYPE html>
<html lang="de">
<head>
<meta charset="utf-8">
<title>Kiesel und Form – Flyer</title>
<link href="https://fonts.googleapis.com/css2?family=Open+Sans:wght@400;600;700&display=swap" rel="stylesheet">
<style>
:root{
  --green:#8dbb25;
  --green-dark:#6f9a16;
  --grey:#4a4a4a;
  --text:#3c3c3c;
  --white:#ffffff;
  --stage:#c6c6c6;
}
*{margin:0;padding:0;box-sizing:border-box}
html,body{width:1200px;height:675px;overflow:hidden;background:var(--stage);font-family:"Open Sans",Arial,sans-serif;color:var(--text)}
.label{position:absolute;top:18px;font-size:19px;color:#111}
.label--back{left:76px}
.label--front{right:58px}
.page{position:absolute;top:52px;width:532px;height:531px;background:var(--white);overflow:hidden}
.page--back{left:78px}
.page--front{left:610px}

/* back page */
.back-band{position:absolute;left:0;top:0;width:100%;height:55px;background:var(--green)}
.back-title{position:absolute;left:32px;top:26px;font-size:17px;font-weight:700;color:var(--white);text-decoration:underline;text-underline-offset:2px}
.copy{position:absolute;left:32px;font-size:11.2px;line-height:12.8px;color:var(--text)}
.copy--url{left:0;width:520px;text-align:center;font-weight:700}
.copy strong{font-weight:700}
.imprint{position:absolute;left:32px;top:491px;font-size:7px;line-height:8.7px;color:var(--text)}
.imprint small{font-size:5.6px}
.thumb{position:absolute;border:1px solid #d8d8d8;box-shadow:1px 1px 2px rgba(0,0,0,.25)}
.thumb--book-a{left:34px;top:232px;width:80px;height:62px;background:linear-gradient(180deg,#7fa05a,#c8cfc4)}
.thumb--book-b{left:134px;top:232px;width:80px;height:62px;background:linear-gradient(180deg,#9aa86a,#c9b9a2)}
.thumb--book-c{left:231px;top:232px;width:80px;height:62px;background:linear-gradient(180deg,#e8ede6,#7c9a4e)}
.thumb--tray{left:329px;top:231px;width:152px;height:63px;background:linear-gradient(180deg,#f1efeb,#dcd8d2);border:none;box-shadow:none}
.thumb--moss{left:303px;top:366px;width:83px;height:55px;background:var(--white);box-shadow:none;border-color:#aaa}
.thumb--moss div{position:absolute;inset:6px;background:linear-gradient(135deg,#3c6a22,#6d9a3a)}
.thumb--fern{left:398px;top:366px;width:83px;height:55px;background:var(--white);box-shadow:none;border-color:#aaa}
.thumb--fern div{position:absolute;left:20px;top:4px;width:46px;height:46px;background:radial-gradient(circle,#2f7a36,#1d4f22 60%,transparent 72%)}

/* front page */
.front-strip{position:absolute;left:0;top:90px;width:32px;height:441px;background:linear-gradient(180deg,#3d5a2c,#6c8a4a 50%,#2e4424)}
.front-column{position:absolute;left:32px;top:90px;width:165px;height:441px;background:var(--green)}
.front-topbar{position:absolute;left:32px;top:0;width:165px;height:25px;background:var(--green)}
.brand{position:absolute;left:32px;top:34px;width:170px;display:flex;align-items:center;gap:7px}
.brand-mark{width:24px;height:24px;background:var(--grey)}
.brand-name{font-size:16px;font-weight:600;color:var(--grey);line-height:1.1}
.brand-claim{position:absolute;left:32px;top:76px;font-size:9px;color:var(--green)}
.claim{position:absolute;left:40px;top:411px;width:150px;border-top:1px solid var(--white);border-bottom:1px solid var(--white);padding:3px 0 3px 0;color:#eef6d9;font-size:13.4px;font-weight:700;line-height:16px}
.front-photo{position:absolute;left:197px;top:90px;width:335px;height:441px;background:linear-gradient(180deg,#8fb6dc 0%,#c9d6df 22%,#b9c2b4 45%,#8b9a7a 70%,#dfe2e0 100%)}
.panel{position:absolute;left:216px;top:129px;width:284px;height:283px;background:rgba(255,255,255,.72)}
.product{position:absolute;width:90px}
.product-img{width:90px;height:89px;border:1px solid #888}
.product-name{display:flex;align-items:center;gap:4px;margin-top:3px;font-size:12.2px;color:var(--grey)}
.product-name::before{content:"";width:5px;height:5px;background:var(--green);transform:rotate(45deg)}
.product--screen{left:15px;top:15px}
.product--screen .product-img{background:linear-gradient(90deg,#ecebe6 60%,#7fa36a)}
.product--pots{left:179px;top:15px}
.product--pots .product-img{background:linear-gradient(180deg,#5b6167,#3f4449)}
.product--acc{left:15px;top:167px}
.product--acc .product-img{background:linear-gradient(180deg,#3a302b,#e9e7e4)}
.product--books{left:179px;top:167px}
.product--books .product-img{background:linear-gradient(180deg,#f4f4f4,#86a55c 50%,#f4f4f4)}
</style>
</head>
<body>
<div class="label label--back">Rückseite</div>
<div class="label label--front">Titelseite</div>

<section class="page page--back">
  <div class="back-band"></div>
  <h1 class="back-title">Ihr Shop für moderne Gartengestaltung</h1>

  <p class="copy" style="top:82px">Bei uns finden Sie ausgewählte Artikel für den modernen Garten, die es im<br>Baumarkt oder Gartencenter nicht gibt. Hergestellt in kleinen und mittelständi-<br>schen Manufakturen – mit hoher Qualität und viel Liebe zum Detail gefertigt.</p>
  <p class="copy" style="top:122px">Besuchen Sie uns unter:</p>
  <p class="copy copy--url" style="top:147px">www.kiesel-und-form.de</p>
  <p class="copy" style="top:173px">um unser ganzes Sortiment zu entdecken.</p>
  <p class="copy" style="top:197px">Bei uns finden Sie auch ausgewählte Bücher sowie Accessoires<br>für die moderne Gartengestaltung:</p>

  <div class="thumb thumb--book-a" role="img" aria-label="Buchcover mit kleinem modernen Garten"></div>
  <div class="thumb thumb--book-b" role="img" aria-label="Buchcover zu Terrassen und Sitzplätzen"></div>
  <div class="thumb thumb--book-c" role="img" aria-label="Buchcover zu Dachterrassen und Balkonen"></div>
  <div class="thumb thumb--tray" role="img" aria-label="Weiße Pflanzschalen aus Beton"></div>

  <p class="copy" style="top:316px">Holen Sie sich ein Stück Garten ins Haus. Für diese Pflanzenbilder – erhältlich in<br>verschiedenen Größen – werden tatsächlich echte Pflanzen verwendet, die durch<br>ein spezielles ökologisches Konservierungsverfahren dauerhaft haltbar gemacht<br>werden.</p>
  <p class="copy" style="top:380px">Dadurch behalten die Pflanzen ihr lebendiges<br>Aussehen, sie brauchen aber kein Licht und<br>kein Wasser mehr.</p>

  <div class="thumb thumb--moss" role="img" aria-label="Gerahmtes Moosbild"><div></div></div>
  <div class="thumb thumb--fern" role="img" aria-label="Pflanzenbild mit Farnen"><div></div></div>

  <p class="copy" style="top:442px"><strong>Service:</strong><br>Kontaktieren Sie uns, wenn Sie spezielle Wünschen haben –<br>wir setzen alle Hebel in Bewegung, um Sie zufrieden zu stellen!<br><strong>Telefonische Beratung:</strong> 06441-52 19 83</p>

  <p class="imprint"><strong>Impressum:</strong><br>Kiesel und Form | Marlene Vogt | Lindenweg 7 | 35390 Gießen <small>(Kein Ladengeschäft oder Ausstellungsfläche!)</small><br>Telefon: 06441-521 984 | kontakt@kiesel-und-form.de | www.kiesel-und-form.de</p>
</section>

<section class="page page--front">
  <div class="front-topbar"></div>
  <div class="brand"><span class="brand-mark"></span><span class="brand-name">Kiesel und Form</span></div>
  <p class="brand-claim">Produkte für den modernen Garten</p>

  <div class="front-strip" role="img" aria-label="Berankte Hauswand mit Grün"></div>
  <div class="front-column"></div>
  <p class="claim">Hier kaufen, was<br>es in Baumarkt<br>und Gartencenter<br>nicht gibt!<br>kiesel-und-form.de</p>

  <div class="front-photo" role="img" aria-label="Innenhof mit bepflanzten Balkonen und weißer Fassade"></div>
  <div class="panel">
    <div class="product product--screen"><div class="product-img" role="img" aria-label="Weißer Sichtschutz mit Lochmuster"></div><p class="product-name">Sichtschutz</p></div>
    <div class="product product--pots"><div class="product-img" role="img" aria-label="Graue Pflanzgefäße vor Holzwand"></div><p class="product-name">Pflanzgefäße</p></div>
    <div class="product product--acc"><div class="product-img" role="img" aria-label="Aufbewahrungskörbe in Braun und Weiß"></div><p class="product-name">Accessoires</p></div>
    <div class="product product--books"><div class="product-img" role="img" aria-label="Gartenbuch mit modernem Garten"></div><p class="product-name">Bücher</p></div>
  </div>
</section>
</body>
</html>
```